Front & Back cover design for timber flooring brochure - A4 size

I need a design for the front and back cover of an A4 sized brochure for a timber and concrete flooring company called "Kestrel Row Floors". The front cover should include the logo (attached), and an image + tagline for each of the three products/services that they offer which are:

1. Timber Flooring
2. Concrete Grinding & Sealing
3. Floor sanding (i have attached a photo for each of these three - however feel free to use other images if you feel they are better).

The back cover should be simple, perhaps just a continuation of the colour or graphic scheme on the front with the company contact details at the bottom.

Industry/Entity Type

Flooring

Requirements
Must have
• front cover has to have the logo with an image and text of the 3 services described. You can use the images attached or your own.

```html
<!DOCTYPE html>
<html lang="en">
<head>
<meta charset="utf-8">
<title>Kestrel Row Floors – Brochure Covers</title>
<link rel="stylesheet" href="https://fonts.googleapis.com/css2?family=Audiowide&family=Source+Sans+3:wght@300&display=swap">
<style>
  :root {
    --canvas: #f1ede7;
    --paper: #ffffff;
    --wood-light: #d99a4a;
    --wood-mid: #b86f2a;
    --wood-deep: #6b3512;
    --wood-dark: #1e0c04;
    --ink: #0d0905;
    --body-text: #fbf1e0;
  }
  * { margin: 0; padding: 0; box-sizing: border-box; }
  html, body { width: 1200px; height: 839px; overflow: hidden; }
  body {
    background: var(--canvas);
    position: relative;
    font-family: "Source Sans 3", sans-serif;
  }

  .page { position: absolute; top: 0; height: 839px; overflow: hidden; }
  .page--front { left: 0; width: 578px; background: var(--paper); }
  .page--back { left: 600px; width: 600px; }

  .wood-backdrop { position: absolute; }
  .page--front .wood-backdrop {
    left: 0; top: 138px; width: 578px; height: 701px;
    background:
      linear-gradient(180deg, rgba(255,255,255,0.85) 0%, rgba(255,255,255,0) 7%),
      linear-gradient(180deg, var(--wood-light) 8%, var(--wood-mid) 55%, var(--wood-deep) 78%, var(--wood-dark) 100%);
  }
  .page--back .wood-backdrop {
    inset: 0;
    background:
      radial-gradient(ellipse at 85% 55%, rgba(60,20,5,0.55) 0%, rgba(60,20,5,0) 45%),
      linear-gradient(180deg, var(--wood-light) 0%, var(--wood-mid) 50%, var(--wood-deep) 82%, var(--wood-dark) 100%);
  }

  .brand {
    position: absolute; left: 0; top: 50px; width: 578px;
    text-align: center;
  }
  .brand__name {
    font-family: "Source Sans 3", sans-serif; font-weight: 300; font-size: 40px;
    color: var(--ink); letter-spacing: 1px;
  }

  .display {
    font-family: "Audiowide", sans-serif; color: var(--ink);
    text-transform: uppercase; position: absolute; line-height: 1.05;
    white-space: nowrap;
  }
  .offer-title { left: 18px; top: 178px; font-size: 31px; letter-spacing: 12px; }

  .service-name { font-size: 14px; letter-spacing: 7.5px; left: 55px; }
  .service-name--timber { top: 245px; }
  .service-name--concrete { top: 340px; line-height: 23px; }
  .service-name--sanding { top: 436px; }

  .thumb {
    position: absolute; left: 410px; width: 104px; height: 70px;
    border: 1px solid rgba(255,255,255,0.7);
    box-shadow: 0 6px 8px rgba(0,0,0,0.35);
  }
  .thumb--timber { top: 258px; background: linear-gradient(135deg, #c98d95, #8a4650 55%, #b3747d); }
  .thumb--concrete { top: 354px; background: radial-gradient(circle at 60% 40%, #9aa08c, #59614f 70%, #3f4538); }
  .thumb--sanding { top: 450px; background: linear-gradient(160deg, #d46a2c, #8c3310 60%, #c25a22); }

  .copy {
    position: absolute;
    font-weight: 300; font-size: 17px; line-height: 23.4px;
    color: var(--body-text);
  }
  .page--front .copy { left: 48px; top: 572px; width: 505px; }
  .page--back .copy { left: 45px; width: 525px; }

  .feature-title { left: 28px; font-size: 21px; letter-spacing: 9.3px; }
  .feature-title--timber { top: 48px; }
  .feature-title--concrete { top: 295px; line-height: 25px; }
  .feature-title--sanding { top: 538px; }
  .copy--timber { top: 104px; }
  .copy--concrete { top: 351px; }
  .copy--sanding { top: 597px; }
</style>
</head>
<body>
  <section class="page page--front">
    <div class="wood-backdrop" role="img" aria-label="End-grain timber block flooring background fading into dark wood tones"></div>

    <header class="brand">
      <span class="brand__name">Kestrel Row Floors</span>
    </header>

    <h1 class="display offer-title">Proud to offer</h1>

    <h2 class="display service-name service-name--timber">1. Timber Flooring</h2>
    <div class="thumb thumb--timber" role="img" aria-label="Timber parquet flooring sample"></div>

    <h2 class="display service-name service-name--concrete">2. Concrete Grinding<br>&amp; Sealing</h2>
    <div class="thumb thumb--concrete" role="img" aria-label="Polished and sealed concrete floor"></div>

    <h2 class="display service-name service-name--sanding">3. Floor Sanding</h2>
    <div class="thumb thumb--sanding" role="img" aria-label="Freshly sanded hardwood floorboards"></div>

    <p class="copy">This is sample Text. The resulting slice is true, perfect, vertically grained wood with the annual rings being the evenly distributed Wooden block floors, also known as end block, butcher block and parquet floors have been around as long as someone has had a cross cut saw to cut a tree into rounds or a square beam into blocks. The resulting ‘slice’ is true, perfect, vertically grained&nbsp; wood with the annual rings being the evenly distributed wear surface.</p>
  </section>

  <section class="page page--back">
    <div class="wood-backdrop" role="img" aria-label="Warm timber grain background with flowing dark drapery"></div>

    <h2 class="display feature-title feature-title--timber">1. Timber Flooring</h2>
    <p class="copy copy--timber">This is sample Text. The resulting slice is true, perfect, vertically grained wood with the annual rings being the evenly distributed Wooden block floors, also known as end block, butcher block and parquet floors have been around as long as someone has had a cross cut saw to cut a tree into rounds or a square beam into blocks. The resulting ‘slice’ is true, perfect, vertically grained&nbsp; wood with the annual rings being the evenly distributed wear surface.</p>

    <h2 class="display feature-title feature-title--concrete">2. Concrete Grinding<br>&amp; Sealing</h2>
    <p class="copy copy--concrete">This is sample Text. The resulting slice is true, perfect, vertically grained wood with the annual rings being the evenly distributed Wooden block floors, also known as end block, butcher block and parquet floors have been around as long as someone has had a cross cut saw to cut a tree into rounds or a square beam into blocks. The resulting ‘slice’ is true, perfect, vertically grained&nbsp; wood with the annual rings being the evenly distributed wear surface.</p>

    <h2 class="display feature-title feature-title--sanding">3. Floor Sanding</h2>
    <p class="copy copy--sanding">This is sample Text. The resulting slice is true, perfect, vertically grained wood with the annual rings being the evenly distributed Wooden block floors, also known as end block, butcher block and parquet floors have been around as long as someone has had a cross cut saw to cut a tree into rounds or a square beam into blocks. The resulting ‘slice’ is true, perfect, vertically grained&nbsp; wood with the annual rings being the evenly distributed wear surface.</p>
  </section>
</body>
</html>
```